Building Asset Management and Engineering Services for complex buildings

We provide asset management, project management, and engineering services for complex buildings.
Asset management services include, asset management strategies, plans, risk and conditioning assessments.
The engineering services include building services redesign, project management and commissioning services.

Target Market(s)

architects, government, electrical contractors

Industry/Entity Type

Asset Management

Contact Information for Business Card

KLT van Brommel QTSph, MKOrvia, DGLT, SMVK
Director
Other details such as address please refer to attached file

Font styles to use
Sans Serif

Requirements
Must have
• Fellow and Engineers logo on the back
• * Strategic Planning
• * Design
• * Documentation
• * Project Management
• * Commissioning
• * Assessment/Review
• Must have Engineers logo and wording on the back as well
Nice to have
• Good use of all the logo colours

```html
<!DOCTYPE html>
<html lang="en">
<head>
<meta charset="utf-8">
<title>KVR Advisors – Business Card</title>
<link rel="stylesheet" href="https://fonts.googleapis.com/css2?family=Montserrat:wght@400;500;600;700&display=swap">
<style>
  :root {
    --brand-blue: #4a8cc8;
    --brand-blue-dark: #3c78b0;
    --card-white: #ffffff;
    --ink: #2a2a2a;
    --ink-soft: #5a5a5a;
    --backdrop: #e4e2df;
    --card-shadow: rgba(0, 0, 0, 0.18);
  }
  * { box-sizing: border-box; margin: 0; padding: 0; }
  html, body {
    width: 1200px;
    height: 580px;
    overflow: hidden;
    background: var(--backdrop);
    font-family: "Montserrat", sans-serif;
  }
  .canvas { position: relative; width: 1200px; height: 580px; }

  .card {
    position: absolute;
    top: 140px;
    width: 520px;
    height: 300px;
    background: var(--card-white);
    box-shadow: 0 6px 18px var(--card-shadow);
    overflow: hidden;
  }
  .card--front { left: 45px; }
  .card--back  { left: 635px; }
  .card__bands { position: absolute; inset: 0; width: 100%; height: 100%; }

  /* Company name (set as plain text) */
  .company {
    position: absolute;
    display: flex;
    flex-direction: column;
    color: var(--brand-blue);
  }
  .company__row { display: flex; align-items: center; gap: 12px; }
  .company__dot { border-radius: 50%; background: var(--brand-blue); flex: none; }
  .company__name {
    font-family: "Montserrat", sans-serif;
    font-weight: 600;
    line-height: 1;
    letter-spacing: 0.02em;
  }
  .company__tagline {
    font-weight: 600;
    letter-spacing: 0.08em;
    text-transform: uppercase;
  }

  .card--front .company { left: 30px; top: 124px; }
  .card--front .company__dot { width: 26px; height: 26px; }
  .card--front .company__name { font-size: 40px; }
  .card--front .company__tagline { font-size: 7px; margin-left: 38px; margin-top: 4px; }

  .card--back .company { left: 50%; top: 78px; transform: translateX(-50%); align-items: flex-start; }
  .card--back .company__dot { width: 44px; height: 44px; }
  .card--back .company__name { font-size: 64px; }
  .card--back .company__tagline { font-size: 10px; margin-left: 56px; margin-top: 6px; }

  /* Name plate */
  .nameplate {
    position: absolute;
    left: 268px;
    top: 14px;
    width: 232px;
    height: 46px;
    background: var(--brand-blue);
    color: var(--card-white);
    padding: 6px 12px;
  }
  .nameplate__name { font-size: 15px; font-weight: 600; letter-spacing: 0.04em; }
  .nameplate__role { font-size: 9px; font-weight: 500; text-align: right; margin-right: 60px; }

  /* Contacts */
  .contacts {
    position: absolute;
    left: 276px;
    top: 86px;
    list-style: none;
    color: var(--ink);
    font-size: 10.5px;
    font-weight: 500;
  }
  .contacts__item { display: flex; align-items: flex-start; gap: 18px; min-height: 28px; }
  .contacts__icon { width: 14px; height: 14px; flex: none; fill: var(--brand-blue); stroke: var(--brand-blue); }
  .contacts__text { line-height: 1.3; }

  /* Services and memberships on the back */
  .services {
    position: absolute;
    left: 40px;
    right: 40px;
    top: 196px;
    display: flex;
    flex-wrap: wrap;
    justify-content: center;
    gap: 4px 14px;
    list-style: none;
    color: var(--ink-soft);
    font-size: 9.5px;
    font-weight: 500;
  }
  .services__item::before { content: "• "; color: var(--brand-blue); }
  .memberships {
    position: absolute;
    left: 0;
    right: 0;
    top: 240px;
    display: flex;
    justify-content: center;
    gap: 14px;
  }
  .memberships__badge {
    width: 22px;
    height: 22px;
    border-radius: 4px;
    background: var(--brand-blue);
  }
</style>
</head>
<body>
<main class="canvas">

  <section class="card card--front" aria-label="Business card front">
    <svg class="card__bands" viewBox="0 0 520 300" preserveAspectRatio="none" aria-hidden="true">
      <path d="M70 0 H520 V8 H92 Q78 8 70 0 Z" fill="var(--brand-blue)"/>
      <path d="M0 286 H300 Q330 286 345 272 Q355 264 380 264 H520 V300 H0 Z" fill="var(--brand-blue)"/>
    </svg>

    <div class="nameplate">
      <div class="nameplate__name">Maren Oltvik</div>
      <div class="nameplate__role">CEO</div>
    </div>

    <div class="company">
      <div class="company__row">
        <span class="company__dot"></span>
        <span class="company__name">KVR</span>
      </div>
      <span class="company__tagline">Advisors Nord Pty Ltd</span>
    </div>

    <ul class="contacts">
      <li class="contacts__item">
        <svg class="contacts__icon" viewBox="0 0 14 14" aria-hidden="true"><path d="M1 5 Q7 0 13 5 L11 7 L9 5.5 L5 5.5 L3 7 Z" stroke="none"/><rect x="3" y="7" width="8" height="5" rx="1" stroke="none"/></svg>
        <span class="contacts__text">0361527084</span>
      </li>
      <li class="contacts__item">
        <svg class="contacts__icon" viewBox="0 0 14 14" aria-hidden="true"><rect x="3.5" y="1" width="7" height="12" rx="1" fill="none" stroke-width="1.2"/></svg>
        <span class="contacts__text">0428306915</span>
      </li>
      <li class="contacts__item">
        <svg class="contacts__icon" viewBox="0 0 14 14" aria-hidden="true"><rect x="1" y="3" width="12" height="8" stroke="none"/><path d="M1 3 L7 8 L13 3" fill="none" stroke="#fff" stroke-width="1"/></svg>
        <span class="contacts__text">office.kvr@northmail.com</span>
      </li>
      <li class="contacts__item">
        <svg class="contacts__icon" viewBox="0 0 14 14" aria-hidden="true"><path d="M7 1 A4 4 0 0 1 11 5 C11 8 7 13 7 13 C7 13 3 8 3 5 A4 4 0 0 1 7 1 Z" stroke="none"/><circle cx="7" cy="5" r="1.5" fill="#fff" stroke="none"/></svg>
        <span class="contacts__text">PO box 512K Lindmere east<br>Corvale Region 4471</span>
      </li>
    </ul>
  </section>

  <section class="card card--back" aria-label="Business card back">
    <svg class="card__bands" viewBox="0 0 520 300" preserveAspectRatio="none" aria-hidden="true">
      <path d="M80 0 H520 V60 H512 V22 Q512 8 498 8 H96 Q84 8 80 0 Z" fill="var(--brand-blue)"/>
      <path d="M0 240 H8 V278 Q8 292 22 292 H424 Q436 292 440 300 H0 Z" fill="var(--brand-blue)"/>
    </svg>

    <div class="company">
      <div class="company__row">
        <span class="company__dot"></span>
        <span class="company__name">KVR</span>
      </div>
      <span class="company__tagline">Advisors Nord Pty Ltd</span>
    </div>

    <ul class="services">
      <li class="services__item">Strategic Planning</li>
      <li class="services__item">Design</li>
      <li class="services__item">Documentation</li>
      <li class="services__item">Project Management</li>
      <li class="services__item">Commissioning</li>
      <li class="services__item">Assessment/Review</li>
    </ul>

    <div class="memberships" aria-label="Professional memberships">
      <span class="memberships__badge" role="img" aria-label="Fellow membership badge"></span>
      <span class="memberships__badge" role="img" aria-label="Engineers membership badge"></span>
    </div>
  </section>

</main>
</body>
</html>
```